Pepper Meadow Indian Restaurant - Easter Dinner Buffet

Pepper Meadow is an Indian restaurant located in Perth's northern suburbs. We are offering a Special Easter Dinner buffet which runs during all public holidays.

The key points is
1. 35+ Items on the menu
2. Sea Food ,Goat , Lamb, Chicken Varieties
3. Plenty of options for Vegetarians and Vegans,
4. Available during all Easter Holidays (5:30PM-9:30PM)
5. Only available for Dine In
6. Adult Price $34.50; Kids under 12 eat at $21. Kids under 2 Free

Items on the menu are as below.

S.No Category Item
1 Soup Lentil Soup
2 Veg Starters Saudi Aloo (Potato)
3 Veg Starters Veg Pakora
4 Veg Starters Onion Bhaji
5 Veg Starters Veg Samosa
6 Veg Starters Potato Pakora
7 Veg Starters Chutney Aloo (Potato)
8 NV Starters Tandoori Chicken
9 NV Starters Murg (Chicken) Kali Tikka
10 NV Starters Chicken 65
11 NV Starters Lemon Chicken Tikka
12 Veg Curries Potato Curry
13 Veg Curries Mix Vegetable Curry
14 Veg Curries Mushrool Masala
15 Veg Curries Yellow Dal
16 NV Curries Fish Fry
17 NV Curries Goat Curry
18 NV Curries Butter Chicken
19 NV Curries Lamb Rogan Josh
20 NV Curries Goan Fish Curry
21 NV Curries Special Chicken Curry
22 Rice Prawn Biryani
23 Rice Steamed Rice
24 Rice Saffron Rice
25 Breads Chocolate Naan
26 Breads Butter Naan
27 Breads Garlic Nann
28 Sides Raitha
29 Sides Papadam
30 Sides Salad
31 Dessert Gulab Jamun
32 Dessert Fruit Custard
33 Dessert Semiya Payasam
34 Dessert Coconut Pudding

Industry/Entity Type

Restaurant

Requirements
Must have
• Title
• Easter Buffet - Extravagant Family Buffet

```html
<!DOCTYPE html>
<html lang="en">
<head>
<meta charset="utf-8">
<title>Pepper Meadow Indian Restaurant – Easter Dinner Buffet</title>
<link href="https://fonts.googleapis.com/css2?family=Raleway:wght@400;600;700&display=swap" rel="stylesheet">
<style>
  :root {
    --gold: #fbb326;
    --bg-centre: #7b6f50;
    --bg-mid: #5e5233;
    --bg-edge: #463a1e;
  }
  * { margin: 0; padding: 0; box-sizing: border-box; }
  html, body { width: 794px; height: 1200px; overflow: hidden; }
  body { font-family: "Raleway", sans-serif; color: var(--gold); }
  .menu-board {
    position: relative;
    width: 794px;
    height: 1200px;
    background: radial-gradient(ellipse 60% 55% at 50% 50%, var(--bg-centre) 0%, var(--bg-mid) 55%, var(--bg-edge) 100%);
    overflow: hidden;
  }
  .rule { position: absolute; background: var(--gold); }
  .rule--top { left: 212px; top: 22px; width: 370px; height: 4px; }
  .rule--bottom { left: 212px; top: 1174px; width: 370px; height: 4px; }
  .rule--left { left: 31px; top: 204px; width: 4px; height: 794px; }
  .rule--right { left: 760px; top: 204px; width: 4px; height: 794px; }
  .rule--title { left: 104px; top: 212px; width: 586px; height: 4px; }

  .corner-flourish {
    position: absolute;
    width: 158px;
    height: 164px;
    background: radial-gradient(circle at 50% 50%, rgba(251,179,38,0.28) 0%, rgba(251,179,38,0.10) 55%, rgba(251,179,38,0) 75%);
  }
  .corner-flourish--tl { left: 28px; top: 16px; }
  .corner-flourish--tr { left: 610px; top: 16px; }
  .corner-flourish--bl { left: 28px; top: 1020px; }
  .corner-flourish--br { left: 610px; top: 1020px; }

  .centred {
    position: absolute;
    left: 0;
    width: 794px;
    text-align: center;
    line-height: 1;
    white-space: nowrap;
  }
  .restaurant-name { font-size: 56px; font-weight: 700; letter-spacing: 0.5px; }
  .restaurant-name--first { top: 78px; }
  .restaurant-name--second { top: 144px; }

  .event-title { top: 232px; font-size: 36px; font-weight: 700; }
  .event-tagline { top: 276px; font-size: 20px; font-weight: 600; letter-spacing: 2px; }

  .section-title { font-size: 40px; font-weight: 700; }
  .section-title--menu { top: 318px; }
  .section-title--dessert { top: 766px; }

  .dish-list { position: absolute; list-style: none; }
  .dish-list--left { left: 54px; top: 374px; width: 348px; }
  .dish-list--right { left: 414px; top: 374px; width: 336px; }
  .dish-list--desserts-left { left: 94px; top: 818px; width: 320px; }
  .dish-list--desserts-right { left: 414px; top: 818px; width: 320px; }
  .dish {
    display: flex;
    height: 25px;
    font-size: 15px;
    line-height: 25px;
    white-space: nowrap;
    letter-spacing: -0.1px;
  }
  .dish__category { flex: 0 0 112px; }
  .dish-list--desserts-left .dish__category,
  .dish-list--desserts-right .dish__category { flex-basis: 84px; }

  .highlights { font-size: 15px; font-weight: 600; }
  .highlights--one { top: 882px; }
  .highlights--two { top: 908px; }
  .highlights--three { top: 934px; }

  .price { font-weight: 700; }
  .price--adult { top: 1046px; font-size: 30px; }
  .price--kids { top: 1090px; font-size: 18px; font-weight: 600; }
  .price--dine-in { top: 1120px; font-size: 15px; font-weight: 400; letter-spacing: 1.5px; }
</style>
</head>
<body>
<main class="menu-board">
  <div class="corner-flourish corner-flourish--tl" role="img" aria-label="Gold scrollwork flourish, top left corner"></div>
  <div class="corner-flourish corner-flourish--tr" role="img" aria-label="Gold scrollwork flourish, top right corner"></div>
  <div class="corner-flourish corner-flourish--bl" role="img" aria-label="Gold scrollwork flourish, bottom left corner"></div>
  <div class="corner-flourish corner-flourish--br" role="img" aria-label="Gold scrollwork flourish, bottom right corner"></div>

  <div class="rule rule--top"></div>
  <div class="rule rule--left"></div>
  <div class="rule rule--right"></div>
  <div class="rule rule--bottom"></div>

  <h1>
    <span class="centred restaurant-name restaurant-name--first">PEPPER MEADOW</span>
    <span class="centred restaurant-name restaurant-name--second">INDIAN RESTAURANT</span>
  </h1>
  <div class="rule rule--title"></div>

  <h2 class="centred event-title">EASTER DINNER BUFFET</h2>
  <p class="centred event-tagline">EXTRAVAGANT FAMILY BUFFET</p>

  <h2 class="centred section-title section-title--menu">MENU</h2>
  <ul class="dish-list dish-list--left">
    <li class="dish"><span class="dish__category">SOUP</span><span class="dish__name">LENTIL SOUP</span></li>
    <li class="dish"><span class="dish__category">VEG STARTERS</span><span class="dish__name">SAUDI ALOO (POTATO)</span></li>
    <li class="dish"><span class="dish__category">VEG STARTERS</span><span class="dish__name">VEG PAKORA</span></li>
    <li class="dish"><span class="dish__category">VEG STARTERS</span><span class="dish__name">ONION BHAJI</span></li>
    <li class="dish"><span class="dish__category">VEG STARTERS</span><span class="dish__name">VEG SAMOSA</span></li>
    <li class="dish"><span class="dish__category">VEG STARTERS</span><span class="dish__name">POTATO PAKORA</span></li>
    <li class="dish"><span class="dish__category">VEG STARTERS</span><span class="dish__name">CHUTNEY ALOO (POTATO)</span></li>
    <li class="dish"><span class="dish__category">NV STARTERS</span><span class="dish__name">TANDOORI CHICKEN</span></li>
    <li class="dish"><span class="dish__category">NV STARTERS</span><span class="dish__name">MURG (CHICKEN) KALI TIKKA</span></li>
    <li class="dish"><span class="dish__category">NV STARTERS</span><span class="dish__name">CHICKEN 65</span></li>
    <li class="dish"><span class="dish__category">NV STARTERS</span><span class="dish__name">LEMON CHICKEN TIKKA</span></li>
    <li class="dish"><span class="dish__category">VEG CURRIES</span><span class="dish__name">POTATO CURRY</span></li>
    <li class="dish"><span class="dish__category">VEG CURRIES</span><span class="dish__name">MIX VEGETABLE CURRY</span></li>
    <li class="dish"><span class="dish__category">VEG CURRIES</span><span class="dish__name">MUSHROOM MASALA</span></li>
    <li class="dish"><span class="dish__category">VEG CURRIES</span><span class="dish__name">YELLOW DAL</span></li>
  </ul>
  <ul class="dish-list dish-list--right">
    <li class="dish"><span class="dish__category">NV CURRIES</span><span class="dish__name">FISH FRY</span></li>
    <li class="dish"><span class="dish__category">NV CURRIES</span><span class="dish__name">GOAT CURRY</span></li>
    <li class="dish"><span class="dish__category">NV CURRIES</span><span class="dish__name">BUTTER CHICKEN</span></li>
    <li class="dish"><span class="dish__category">NV CURRIES</span><span class="dish__name">LAMB ROGAN JOSH</span></li>
    <li class="dish"><span class="dish__category">NV CURRIES</span><span class="dish__name">GOAN FISH CURRY</span></li>
    <li class="dish"><span class="dish__category">NV CURRIES</span><span class="dish__name">SPECIAL CHICKEN CURRY</span></li>
    <li class="dish"><span class="dish__category">RICE</span><span class="dish__name">PRAWN BIRYANI</span></li>
    <li class="dish"><span class="dish__category">RICE</span><span class="dish__name">STEAMED RICE</span></li>
    <li class="dish"><span class="dish__category">RICE</span><span class="dish__name">SAFFRON RICE</span></li>
    <li class="dish"><span class="dish__category">BREADS</span><span class="dish__name">CHOCOLATE NAAN</span></li>
    <li class="dish"><span class="dish__category">BREADS</span><span class="dish__name">BUTTER NAAN</span></li>
    <li class="dish"><span class="dish__category">BREADS</span><span class="dish__name">GARLIC NAAN</span></li>
    <li class="dish"><span class="dish__category">SIDES</span><span class="dish__name">RAITHA</span></li>
    <li class="dish"><span class="dish__category">SIDES</span><span class="dish__name">PAPADAM</span></li>
    <li class="dish"><span class="dish__category">SIDES</span><span class="dish__name">SALAD</span></li>
  </ul>

  <h2 class="centred section-title section-title--dessert">DESSERT</h2>
  <ul class="dish-list dish-list--desserts-left">
    <li class="dish"><span class="dish__category">DESSERT</span><span class="dish__name">GULAB JAMUN</span></li>
    <li class="dish"><span class="dish__category">DESSERT</span><span class="dish__name">FRUIT CUSTARD</span></li>
  </ul>
  <ul class="dish-list dish-list--desserts-right">
    <li class="dish"><span class="dish__category">DESSERT</span><span class="dish__name">SEMIYA PAYASAM</span></li>
    <li class="dish"><span class="dish__category">DESSERT</span><span class="dish__name">COCONUT PUDDING</span></li>
  </ul>

  <p class="centred highlights highlights--one">35+ ITEMS · SEAFOOD, GOAT, LAMB &amp; CHICKEN VARIETIES</p>
  <p class="centred highlights highlights--two">PLENTY OF OPTIONS FOR VEGETARIANS &amp; VEGANS</p>
  <p class="centred highlights highlights--three">ALL EASTER PUBLIC HOLIDAYS · 5:30PM – 9:30PM</p>

  <p class="centred price price--adult">ADULTS $34.50</p>
  <p class="centred price price--kids">KIDS UNDER 12 $21 · UNDER 2 FREE</p>
  <p class="centred price price--dine-in">DINE IN ONLY</p>
</main>
</body>
</html>
```